tobrin family medicine business cards

create business cards for 7 family medicine providers and 4 admin using attached logo
2 locations
appointment reminder on back of cards
will provide more info regarding names,addresses, credentials etc once started

```html
<!DOCTYPE html>
<html lang="en">
<head>
<meta charset="utf-8">
<title>Tobrin Family Medicine – Business Cards</title>
<link href="https://fonts.googleapis.com/css2?family=Open+Sans:wght@400;600;700&display=swap" rel="stylesheet">
<style>
  :root {
    --backdrop: #808080;
    --card: #ffffff;
    --navy: #262262;
    --sky: #29a9e0;
    --rule: #8a8a8a;
    --fine: #555555;
  }
  * { margin: 0; padding: 0; box-sizing: border-box; }
  html, body { width: 1200px; height: 1000px; overflow: hidden; }
  body {
    background: var(--backdrop);
    font-family: "Open Sans", Arial, sans-serif;
    position: relative;
  }
  .card {
    position: absolute;
    left: 294px;
    width: 613px;
    height: 352px;
    background: var(--card);
    border-radius: 30px;
    overflow: hidden;
  }
  .card--front { top: 118px; }
  .card--back { top: 528px; }

  /* Front */
  .brand {
    position: absolute;
    left: 0; top: 0; width: 100%; height: 217px;
    display: flex; align-items: center; justify-content: center; gap: 28px;
  }
  .brand__dot {
    width: 118px; height: 118px; border-radius: 50%;
    background: var(--sky);
  }
  .brand__name {
    color: var(--navy);
    font-weight: 700;
    font-size: 46px;
    line-height: 1.05;
    letter-spacing: 0.5px;
  }
  .staff-band {
    position: absolute; left: 0; top: 217px; width: 100%; height: 101px;
    background: var(--sky);
    color: #fff;
    font-weight: 600;
    font-size: 17px;
    line-height: 26.5px;
    text-align: center;
    padding-top: 10px;
  }
  .website {
    position: absolute; left: 0; top: 323px; width: 100%;
    text-align: center;
    color: var(--navy);
    font-weight: 700;
    font-size: 14px;
    display: flex; align-items: center; justify-content: center; gap: 4px;
  }

  /* Back */
  .reminder__title {
    position: absolute; left: 0; top: 48px; width: 100%;
    text-align: center;
    color: var(--navy);
    font-weight: 700;
    font-size: 21px;
  }
  .field {
    position: absolute;
    color: var(--sky);
    font-weight: 700;
    font-size: 23px;
  }
  .field__line {
    position: absolute;
    border-bottom: 1.5px solid var(--rule);
  }
  .date-slash {
    position: absolute; top: 147px;
    color: var(--rule); font-size: 18px;
  }
  .locations-band {
    position: absolute; left: 0; top: 217px; width: 100%; height: 101px;
    background: var(--sky);
    color: #fff;
  }
  .location {
    position: absolute; top: 4px;
    text-align: center;
    font-size: 14px;
    line-height: 17px;
  }
  .location--a { left: 60px; width: 240px; }
  .location--b { left: 290px; width: 260px; }
  .location__name { font-weight: 700; text-transform: uppercase; }
  .location__pin { display: block; margin: 0 auto 2px; }
  .location__phone { display: inline-flex; align-items: center; gap: 4px; }
  .policy {
    position: absolute; left: 0; top: 327px; width: 100%;
    text-align: center;
    font-size: 12px;
    color: var(--fine);
  }
</style>
</head>
<body>

<section class="card card--front">
  <div class="brand">
    <div class="brand__dot"></div>
    <div class="brand__name">Tobrin<br>Family Medicine</div>
  </div>
  <div class="staff-band">
    Dr.Aaron Tobrin • Dr.Marisa Tobrin • Dr.&nbsp; Helen Carver<br>
    Nadine Okafor • Dr.Valentina Roswell • Monica Feldstein<br>
    Lucy Moreno • Sam Hollis • Renata Alvarado-Quinn
  </div>
  <div class="website">
    <svg width="13" height="13" viewBox="0 0 14 14" aria-hidden="true">
      <circle cx="7" cy="7" r="6" fill="none" stroke="#29a9e0" stroke-width="1.4"/>
      <ellipse cx="7" cy="7" rx="2.6" ry="6" fill="none" stroke="#29a9e0" stroke-width="1.2"/>
      <line x1="1" y1="7" x2="13" y2="7" stroke="#29a9e0" stroke-width="1.2"/>
    </svg>
    doctortobrin.com
  </div>
</section>

<section class="card card--back">
  <h2 class="reminder__title">Your next appointment is schedule for:</h2>

  <div class="field" style="left:92px; top:108px;">Name:</div>
  <div class="field__line" style="left:176px; top:130px; width:338px;"></div>

  <div class="field" style="left:92px; top:150px;">Date:</div>
  <div class="field__line" style="left:161px; top:173px; width:185px;"></div>
  <span class="date-slash" style="left:230px;">/</span>
  <span class="date-slash" style="left:272px;">/</span>

  <div class="field" style="left:366px; top:150px;">Time:</div>
  <div class="field__line" style="left:436px; top:173px; width:78px;"></div>

  <div class="locations-band">
    <div class="location location--a">
      <svg class="location__pin" width="10" height="14" viewBox="0 0 10 14" aria-hidden="true">
        <path d="M5 0C2.2 0 0 2.2 0 5c0 3.6 5 9 5 9s5-5.4 5-9C10 2.2 7.8 0 5 0z" fill="#fff"/>
        <circle cx="5" cy="5" r="2" fill="#29a9e0"/>
      </svg>
      <div class="location__name">Brookvale Location</div>
      <div>4821 Harlow Road, Suite 310</div>
      <div>Brookvale, Florida 33020</div>
      <div class="location__phone">
        <svg width="10" height="10" viewBox="0 0 10 10" aria-hidden="true"><path d="M2 0.5l1.6 2.3-1 1.1c.6 1.3 1.6 2.3 2.9 2.9l1.1-1L9 7.4 8 9.4C4 9.2.8 6 .6 2z" fill="#fff"/></svg>
        (555) 214-7730
      </div>
    </div>
    <div class="location location--b">
      <svg class="location__pin" width="10" height="14" viewBox="0 0 10 14" aria-hidden="true">
        <path d="M5 0C2.2 0 0 2.2 0 5c0 3.6 5 9 5 9s5-5.4 5-9C10 2.2 7.8 0 5 0z" fill="#fff"/>
        <circle cx="5" cy="5" r="2" fill="#29a9e0"/>
      </svg>
      <div class="location__name">Ridgeford Location</div>
      <div>1750 N. Meridian Parkway, Suite 105</div>
      <div>Ridgeford, Florida 33040</div>
      <div class="location__phone">
        <svg width="10" height="10" viewBox="0 0 10 10" aria-hidden="true"><path d="M2 0.5l1.6 2.3-1 1.1c.6 1.3 1.6 2.3 2.9 2.9l1.1-1L9 7.4 8 9.4C4 9.2.8 6 .6 2z" fill="#fff"/></svg>
        (555) 382-6194
      </div>
    </div>
  </div>

  <p class="policy">Please give 24 hours notice for cancellations to avoid a $50,00 no show fee.</p>
</section>

</body>
</html>
```